Design a compelling Tarnwell Business Card that will drive people to my site

I want a business card that I can give to people—less to tell them who I am and more to direct them to my website. My website is a portal for Crestlane Aquatics Officials and a place for people who want to become Crestlane Aquatics Officials.
I am uploading my official company logo as well as a business card mockup that I did on my own. Please feel free to completely stray from this design.
I've included a screen recording of the homepage of my website as well.
Target Market(s)
Crestlane Aquatics Officials and people who desire to become one
Contact Information for Business Card
website url
Look and feel
Each slider illustrates characteristics of the customer's brand and the style your logo design should communicate.

```html
<!DOCTYPE html>
<html lang="en">
<head>
<meta charset="utf-8">
<title>Tarnwell Business Card</title>
<link rel="stylesheet" href="https://fonts.googleapis.com/css2?family=Poppins:wght@400;600;700&display=swap">
<style>
  :root {
    --stage: #2c2f34;
    --brand-blue: #283b8c;
    --brand-blue-deep: #22327a;
    --tab-blue: #98acdb;
    --paper: #ffffff;
    --ink: #1d1d22;
    --silver: #c6c9d3;
    --rule: #7f97d4;
  }
  * { box-sizing: border-box; margin: 0; padding: 0; }
  html, body {
    width: 1200px; height: 985px; overflow: hidden;
    background: var(--stage);
    font-family: "Poppins", sans-serif;
  }
  .stage {
    position: relative; width: 1200px; height: 985px;
  }
  .card {
    position: absolute; left: 300px;
    width: 600px; height: 343px;
    border-radius: 22px; overflow: hidden;
    box-shadow: 0 14px 30px rgba(0,0,0,0.35);
  }
  /* front */
  .card-front { top: 110px; background: var(--paper); }
  .front-panel {
    position: absolute; left: 0; top: 0; bottom: 0; width: 245px;
    background: var(--brand-blue);
  }
  .brand-lockup {
    position: absolute; left: 0; top: 82px; width: 245px;
    display: flex; align-items: center; justify-content: center; gap: 10px;
    color: var(--paper); font-weight: 600; font-size: 40px; letter-spacing: -0.5px;
  }
  .brand-dot {
    width: 18px; height: 18px; border-radius: 50%; background: var(--tab-blue);
  }
  .identity { position: absolute; left: 320px; top: 60px; }
  .identity-name { color: var(--brand-blue); font-weight: 700; font-size: 29px; line-height: 1.1; }
  .identity-role { color: var(--ink); font-weight: 400; font-size: 16px; margin-top: 4px; }
  .identity-rule { width: 70px; height: 2px; background: var(--rule); margin-top: 8px; }
  .contact-tab {
    position: absolute; left: 205px; top: 185px; width: 80px; height: 128px;
    background: var(--tab-blue); border-radius: 0 12px 12px 12px;
    display: flex; flex-direction: column; align-items: center; justify-content: space-evenly;
  }
  .contact-tab::before {
    content: ""; position: absolute; left: 0; top: -10px; width: 22px; height: 10px;
    background: var(--tab-blue); border-radius: 6px 6px 0 0;
  }
  .contact-icon {
    width: 26px; height: 26px; border-radius: 50%; background: var(--brand-blue);
    display: flex; align-items: center; justify-content: center;
  }
  .contact-list {
    position: absolute; left: 302px; top: 190px; list-style: none;
    color: var(--ink); font-size: 19px; line-height: 38px;
  }
  /* back */
  .card-back { top: 532px; background: var(--brand-blue); }
  .back-lockup {
    position: absolute; inset: 0;
    display: flex; align-items: center; justify-content: center; gap: 14px;
    color: var(--silver); font-weight: 600; font-size: 58px; letter-spacing: -1px;
  }
  .back-dot { width: 26px; height: 26px; border-radius: 50%; background: var(--silver); }
</style>
</head>
<body>
<main class="stage">
  <section class="card card-front" aria-label="Business card front">
    <div class="front-panel">
      <div class="brand-lockup"><span class="brand-dot"></span><span>tarnwell</span></div>
    </div>
    <div class="identity">
      <p class="identity-name">Marcus Whitley</p>
      <p class="identity-role">CEO &amp; Founder</p>
      <div class="identity-rule"></div>
    </div>
    <div class="contact-tab">
      <span class="contact-icon">
        <svg width="14" height="14" viewBox="0 0 24 24" fill="#fff"><path d="M6.6 10.8a15 15 0 0 0 6.6 6.6l2.2-2.2a1 1 0 0 1 1-.25 11.4 11.4 0 0 0 3.6.57 1 1 0 0 1 1 1V20a1 1 0 0 1-1 1A17 17 0 0 1 3 4a1 1 0 0 1 1-1h3.5a1 1 0 0 1 1 1c0 1.25.2 2.45.57 3.57a1 1 0 0 1-.25 1z"/></svg>
      </span>
      <span class="contact-icon">
        <svg width="14" height="14" viewBox="0 0 24 24" fill="none" stroke="#fff" stroke-width="2"><rect x="3" y="5" width="18" height="14" rx="1"/><path d="M3 6l9 7 9-7"/></svg>
      </span>
      <span class="contact-icon">
        <svg width="14" height="14" viewBox="0 0 24 24" fill="none" stroke="#fff" stroke-width="2"><rect x="7" y="3" width="10" height="18" rx="2"/><path d="M11 18h2"/></svg>
      </span>
    </div>
    <ul class="contact-list">
      <li>(555 014-2270</li>
      <li>marcus@tarnwell.com</li>
      <li>www.tarnwell.com</li>
    </ul>
  </section>

  <section class="card card-back" aria-label="Business card back">
    <div class="back-lockup"><span class="back-dot"></span><span>tarnwell.com</span></div>
  </section>
</main>
</body>
</html>
```